DUNOLA Label for Whole & Sliced Mushrooms in Glass Jars

- Brand Name: DUNOLA
- Product Type:
-Whole Mushrooms, Whole Mushrooms

-Sliced Mushrooms, Sliced Mushrooms

-Packaging Format:
Glass jar 340ml
Wrap-around label with partial transparency preferred

-Design Objective:
Create a visually appealing and modern label that highlights freshness, cleanliness, and the premium quality of the mushrooms, while showingcasing the jar's transparency.

-Visual Elements to Include:
High-quality photo or illustration of the mushrooms (whole or sliced)

Clean and minimalist background to let the real product show through the jar

Natural touches (wooden cutting board, leaves, or forest imagery)

Visual indicator to distinguish Whole vs Sliced (eg , icon or color band)

Transparent section or cut-out in label to reveal product insid

-Product name:

"Whole Mushrooms" "Champignons entiers"

"Sliced Mushrooms " "Champignons tranchés"

Ingredients:

Mushrooms, water, salt, citric acid

Net weight & drained weight (e.g. 340ml / 180g drained)

Nutrition facts table

Barcode

Bilingual text (French / English)

“Ideal for salads, pizzas, pasta”

-Tone & Style:
Natural & Fresh

Modern yet simple

Trustworthy, clean, and gourmet

Target Market(s)

United States and Europe

Industry/Entity Type

Food

Font styles to use
Sans Serif
Decorative

Colors
0054AA
0677BA
7BADD7
CADEEF
E8F1F8
0094D4
00A9DD
6FCCEA
C7EBF8
E9F6FB
00AB8E
00BBA5
67D7C9
C6EFE9
E9F9F6
59FF00
82FF00
B8FF75
E3FFCB
F4FFEA
FFF300
FFF600
FEFA6F
FFFEC7
FFFEE8
FFC000
F8CF3A
FAE287
FDF2CF
FEFAEE
F0912C
F2A743
F7CA91
FBE8D2
FDF5EE
EE7325
F08F49
F5BC92
FAE3D3
FDF4ED
EB3D1F
EC4F4E
F09395
F8D3D4
FCEDEE
E54698
E96AAD
F1A4CE
F9D9EA
FCEFF6
A7469A
B969AE
D3A5CF
EDDBEB
F8F0F9
6B429C
8869AF
B7A5CE
E3DAEB
F3F0F8

Requirements
Must have
• Visual Elements to Include: High-quality photo or illustration of the mushrooms (whole or sliced) Clean and minimalist background to let the real product show through the jar Natural touches (wooden cutting board, leaves, or forest imagery) Visual indicator to distinguish Whole vs Sliced (eg, icon or color band) Transparent section or cut-out in label to reveal product insid -Product name: "Whole Mushrooms" "Sliced Mushrooms"
Nice to have
• Transparent section or cut-out in label to reveal product inside

```html
<!DOCTYPE html>
<html lang="en">
<head>
<meta charset="utf-8">
<title>DUNOLA Mushroom Labels</title>
<link rel="stylesheet" href="https://fonts.googleapis.com/css2?family=Bebas+Neue&family=Lobster&family=Poppins:wght@600&display=swap">
<style>
  :root {
    --backdrop: #4b4b4b;
    --orange-deep: #f0912c;
    --orange-light: #f8cf3a;
    --gold: #d9a521;
    --gold-light: #fae287;
    --navy: #2f2c6e;
    --white: #ffffff;
    --wood-dark: #3b2a1c;
    --wood-mid: #8a5a34;
    --cream-dark: #6b5a45;
    --cream-light: #efe4d2;
  }
  * { margin: 0; padding: 0; box-sizing: border-box; }
  html, body {
    width: 1200px;
    height: 2284px;
    overflow: hidden;
    background: var(--backdrop);
  }
  .canvas {
    position: relative;
    width: 1200px;
    height: 2284px;
  }
  .label {
    position: absolute;
    left: 100px;
    width: 1000px;
    height: 540px;
    border-radius: 6px;
    overflow: hidden;
    box-shadow: 0 10px 30px rgba(0,0,0,0.25);
  }
  .label--whole { top: 300px; }
  .label--sliced { top: 1350px; }
  .label__art {
    position: absolute;
    inset: 0;
    width: 100%;
    height: 100%;
  }
  .label__brand {
    position: absolute;
    top: 36px;
    left: 0;
    width: 100%;
    text-align: center;
    font-family: "Bebas Neue", sans-serif;
    font-size: 104px;
    line-height: 1;
    letter-spacing: 4px;
    color: var(--navy);
  }
  .label__variant {
    position: absolute;
    top: 150px;
    left: 0;
    width: 100%;
    text-align: center;
    font-family: "Lobster", cursive;
    font-size: 92px;
    line-height: 1;
    color: var(--white);
  }
  .label__product {
    position: absolute;
    top: 238px;
    left: 0;
    width: 100%;
    text-align: center;
    font-family: "Bebas Neue", sans-serif;
    font-size: 124px;
    line-height: 1;
    letter-spacing: 2px;
    color: var(--white);
  }
  .label__volume {
    position: absolute;
    bottom: 0;
    left: 50%;
    transform: translateX(-50%);
    width: 130px;
    height: 36px;
    border-radius: 6px 6px 0 0;
    background: var(--orange-deep);
    font-family: "Poppins", sans-serif;
    font-weight: 600;
    font-size: 24px;
    line-height: 38px;
    text-align: center;
    color: var(--white);
  }
</style>
</head>
<body>
<main class="canvas">

  <section class="label label--whole">
    <svg class="label__art" viewBox="0 0 1000 540" aria-hidden="false">
      <defs>
        <linearGradient id="wholeOrange" x1="0" y1="0" x2="1" y2="0">
          <stop offset="0" stop-color="#f0912c"/>
          <stop offset="1" stop-color="#f8b23a"/>
        </linearGradient>
        <linearGradient id="wholePhoto" x1="0" y1="0" x2="1" y2="1">
          <stop offset="0" stop-color="#3b2a1c"/>
          <stop offset="0.5" stop-color="#8a5a34"/>
          <stop offset="1" stop-color="#5a3a22"/>
        </linearGradient>
        <linearGradient id="wholeGold" x1="0" y1="0" x2="1" y2="0">
          <stop offset="0" stop-color="#d9a521"/>
          <stop offset="0.5" stop-color="#fae287"/>
          <stop offset="1" stop-color="#d9a521"/>
        </linearGradient>
      </defs>
      <rect class="label__field" width="1000" height="540" fill="url(#wholeOrange)"/>
      <path class="label__photo" role="img" aria-label="Photo of whole brown mushrooms with parsley on a wooden board"
            d="M0 380 Q500 420 1000 330 L1000 540 L0 540 Z" fill="url(#wholePhoto)"/>
      <path class="label__band" d="M0 380 Q500 420 1000 330" fill="none" stroke="url(#wholeGold)" stroke-width="10"/>
      <circle class="label__type-icon" role="img" aria-label="Icon of whole mushrooms"
              cx="940" cy="330" r="44" fill="#efe4d2" stroke="#ffffff" stroke-width="6"/>
    </svg>
    <div class="label__brand">DUNOLA</div>
    <div class="label__variant">Whole</div>
    <div class="label__product">MUSHROOMS</div>
    <div class="label__volume">340ml</div>
  </section>

  <section class="label label--sliced">
    <svg class="label__art" viewBox="0 0 1000 540" aria-hidden="false">
      <defs>
        <linearGradient id="slicedOrange" x1="0" y1="0" x2="1" y2="0">
          <stop offset="0" stop-color="#f0912c"/>
          <stop offset="1" stop-color="#f8b23a"/>
        </linearGradient>
        <linearGradient id="slicedPhoto" x1="0" y1="0" x2="1" y2="1">
          <stop offset="0" stop-color="#6b5a45"/>
          <stop offset="0.45" stop-color="#efe4d2"/>
          <stop offset="1" stop-color="#c9b394"/>
        </linearGradient>
        <linearGradient id="slicedGold" x1="0" y1="0" x2="1" y2="0">
          <stop offset="0" stop-color="#d9a521"/>
          <stop offset="0.5" stop-color="#fae287"/>
          <stop offset="1" stop-color="#d9a521"/>
        </linearGradient>
      </defs>
      <rect class="label__field" width="1000" height="540" fill="url(#slicedOrange)"/>
      <path class="label__photo" role="img" aria-label="Photo of sliced white mushrooms in a wooden bowl"
            d="M0 380 Q500 420 1000 330 L1000 540 L0 540 Z" fill="url(#slicedPhoto)"/>
      <path class="label__band" d="M0 380 Q500 420 1000 330" fill="none" stroke="url(#slicedGold)" stroke-width="10"/>
      <circle class="label__type-icon" role="img" aria-label="Icon of sliced mushrooms"
              cx="940" cy="330" r="44" fill="#efe4d2" stroke="#ffffff" stroke-width="6"/>
    </svg>
    <div class="label__brand">DUNOLA</div>
    <div class="label__variant">Sliced</div>
    <div class="label__product">MUSHROOMS</div>
    <div class="label__volume">340ml</div>
  </section>

</main>
</body>
</html>
```